Poster Design Project for Bar in Melbourne

Project Description:
JOB DESCRIPTION:

PROJECT: A1 Poster

We are a popular Beer Hall and Wine Room in Melbourne. www.corbelmarsh.com.au We need a poster to promote our up and coming 1st Birthday and we are wanting the look and feel to be like a music festival poster with the head line act and smaller acts being underneath - see example attached. The poster has to be eye catching.
All information below needs to be included - good use of colour!

NAME OF THE EVENT: Corbels 1st Birthday! (Headline)

WHATS GOING ON: Opening of Pemberlows, Suckling Pig, 4 new beers on tap, New summer cocktails,

DATE OF EVENT: 2nd December

TIME: Doors open at Midday

ADDRESS: 82 Tavish Rd, Elmsworth
PHONE: 9476-2035
EMAIL: info@corbelmarsh.com.au
WEB: www.corbelmarsh.com.au

-

IMAGES: Images must be high resolution or vector to ensure clarity and quality is of the highest standard.

POSTER PRODUCTION: Poster must be created in illustrator or photoshop in case any editing needs to be done. Please provide 3mm internal and external bleed

Update images to be used in the poster design - they are all high res so no need for you to search. Those that I have contacted direct for specific edits please use these images also.

Cheers

Target Market(s)

Demographic is inner city 25 - 45 both men and women, enjoy drinking beer and wine and great food. Social people that love mingling and being out!

Industry/Entity Type

Festival

Requirements
Must have
• Use all imagery below - all are high res quality, poster needs to be eye catching and include company logo etc

```html
<!DOCTYPE html>
<html lang="en">
<head>
<meta charset="utf-8">
<title>Corbels 1st Birthday</title>
<link href="https://fonts.googleapis.com/css2?family=Archivo:wdth,wght@62..125,400..900&family=Archivo+Black&display=swap" rel="stylesheet">
<style>
  :root {
    --paper: #ffffff;
    --ink: #0d0d0d;
    --red: #ec1c24;
    --orange: #f3893a;
    --frame: #bdbdbd;
  }
  html, body { margin: 0; padding: 0; overflow: hidden; background: var(--paper); }
  .poster {
    position: relative;
    width: 848px; height: 1200px;
    background: var(--paper);
    box-sizing: border-box;
    border: 1px solid var(--frame);
    overflow: hidden;
    font-family: "Archivo", "Arial", sans-serif;
  }
  .panel { position: absolute; }
  .panel--red { left: 14px; top: 78px; width: 378px; height: 1100px; background: var(--red); }
  .panel--orange { left: 392px; top: 177px; width: 439px; height: 1001px; background: var(--orange); }

  .glass-art {
    position: absolute; left: 138px; top: 300px;
    width: 402px; height: 760px;
  }

  .headline {
    position: absolute; margin: 0; white-space: nowrap;
    font-family: "Archivo", "Arial Black", sans-serif;
    font-weight: 900; font-stretch: 90%;
    color: var(--ink); line-height: 1; text-transform: uppercase;
  }
  .headline__name {
    left: 10px; top: 10px; font-size: 72px; letter-spacing: -1px;
    -webkit-text-stroke: 2px var(--paper); paint-order: stroke fill;
  }
  .headline__numeral {
    left: 394px; top: 56px; font-size: 170px;
    transform: scaleX(0.32); transform-origin: left top;
  }
  .headline__suffix { left: 420px; top: 158px; font-size: 44px; font-stretch: 80%; }
  .headline__birthday { right: 8px; top: 142px; font-size: 54px; font-stretch: 85%; letter-spacing: -0.5px; }

  .attractions {
    position: absolute; right: 37px; top: 618px;
    margin: 0; padding: 0; list-style: none; text-align: right;
    color: var(--ink); font-weight: 700; font-size: 19px; line-height: 32px;
    text-transform: uppercase;
  }

  .venue {
    position: absolute; left: 54px; top: 720px; width: 260px;
    color: var(--ink); font-weight: 700; text-align: center; line-height: 1;
  }
  .venue__name { display: block; font-size: 60px; font-stretch: 75%; letter-spacing: 2px; }
  .venue__tagline { display: block; margin-top: 8px; font-size: 14px; font-stretch: 80%; letter-spacing: 1px; border-top: 2px solid var(--ink); padding-top: 6px; }

  .date {
    position: absolute; right: 531px; top: 852px; margin: 0;
    color: var(--paper); font-weight: 900; font-stretch: 80%;
    text-align: right; line-height: 1;
  }
  .date__day { display: block; font-size: 82px; letter-spacing: -2px; }
  .date__month { display: block; font-size: 58px; letter-spacing: -1px; margin-top: -4px; }

  .doors {
    position: absolute; left: 32px; top: 1000px;
    padding: 7px 10px; background: var(--paper);
    color: var(--ink); font-weight: 800; font-stretch: 85%; font-size: 22px; line-height: 1;
    transform: rotate(-5deg); transform-origin: left top;
    white-space: nowrap;
  }

  .contact {
    position: absolute; right: 37px; top: 966px;
    margin: 0; font-style: normal; text-align: right;
    color: var(--paper); font-weight: 700; font-size: 19px; line-height: 30px;
  }
  .contact span { display: block; }
</style>
</head>
<body>
  <main class="poster">
    <div class="panel panel--red"></div>
    <div class="panel panel--orange"></div>

    <svg class="glass-art" viewBox="0 0 402 760" role="img" aria-label="Illustration of a tall beer glass overflowing with foam and sound waves">
      <rect x="0" y="0" width="402" height="350" rx="40" fill="#ffffff"/>
      <rect x="217" y="300" width="160" height="460" rx="30" fill="#ffffff"/>
    </svg>

    <h1 class="headline headline__name">Corbels</h1>
    <span class="headline headline__numeral">1</span>
    <span class="headline headline__suffix">st</span>
    <span class="headline headline__birthday">Birthday!</span>

    <ul class="attractions">
      <li>Opening of Pemberlows</li>
      <li>Suckling Pig</li>
      <li>4 New Beers on Tap</li>
      <li>New Summer Cocktails</li>
    </ul>

    <div class="venue">
      <span class="venue__name">CORBEL</span>
      <span class="venue__tagline">BEER HALL &amp; WINE ROOM</span>
    </div>

    <p class="date">
      <span class="date__day">2nd</span>
      <span class="date__month">December</span>
    </p>

    <div class="doors">Doors open at Midday</div>

    <address class="contact">
      <span>82 Tavish Rd, Elmsworth</span>
      <span>9476-2035</span>
      <span>info@corbelmarsh.com.au</span>
      <span>www.corbelmarsh.com.au</span>
    </address>
  </main>
</body>
</html>
```